4 Page Music Brochure design

We need assistance in designing a 4 Page A4 (A3 folded) Brochure promoting International Music Tour options for school groups. We have included text in the brief as well as images to be used in the brochure.

```html
<!DOCTYPE html>
<html lang="en">
<head>
<meta charset="utf-8">
<title>Meridian Group Travel – Music Tours Brochure</title>
<link href="https://fonts.googleapis.com/css2?family=Open+Sans:wght@400;600;700;800&display=swap" rel="stylesheet">
<style>
  :root {
    --stage: #d6d6d6;
    --paper: #ffffff;
    --ink: #231f20;
    --ink-soft: #2d2a2b;
    --brand-red: #c1272d;
    --brand-red-dark: #9e1c22;
    --text-grey: #555555;
    --text-light: #e6e6e6;
  }
  * { box-sizing: border-box; margin: 0; padding: 0; }
  html, body { width: 1200px; height: 1200px; overflow: hidden; }
  body {
    background: var(--stage);
    font-family: "Open Sans", Arial, sans-serif;
    position: relative;
  }
  .spread {
    position: absolute;
    left: 200px;
    width: 800px;
    height: 566px;
    background: var(--paper);
    box-shadow: 0 6px 18px rgba(0,0,0,.25);
    overflow: hidden;
  }
  .spread--outer { top: 24px; }
  .spread--inner { top: 610px; }
  .spread-art { position: absolute; inset: 0; width: 800px; height: 566px; }
  .fold { position: absolute; top: 0; left: 399px; width: 2px; height: 100%; background: rgba(0,0,0,.08); }

  .brand-name {
    position: absolute;
    color: var(--paper);
    font-weight: 800;
    text-transform: uppercase;
    line-height: .95;
    letter-spacing: -.5px;
  }
  .brand-name span { display: block; }
  .cover-brand { right: 36px; top: 22px; font-size: 27px; text-align: right; }
  .back-brand { left: 70px; top: 452px; font-size: 27px; }
  .inner-brand { left: 16px; top: 26px; font-size: 20px; }

  .contact-list { position: absolute; left: 72px; top: 520px; list-style: none; color: var(--paper); font-size: 9px; line-height: 13px; }
  .contact-list li { display: flex; align-items: center; gap: 6px; }
  .contact-icon { width: 9px; height: 9px; border-radius: 50%; background: var(--brand-red); display: inline-flex; }

  .copy { position: absolute; font-size: 7.2px; line-height: 1.4; }
  .copy--dark { color: var(--text-grey); }
  .copy--light { color: var(--text-light); }
  .intro-lead { left: 16px; top: 76px; width: 138px; }
  .intro-focus { left: 212px; top: 14px; width: 178px; }
  .intro-body { left: 182px; top: 76px; width: 208px; }

  .service-list { position: absolute; left: 110px; top: 248px; width: 280px; list-style: none; font-size: 7.2px; line-height: 12px; color: var(--text-grey); }
  .service-list li::before { content: ""; display: inline-block; width: 4px; height: 4px; border-radius: 50%; background: var(--brand-red); margin-right: 5px; vertical-align: middle; }

  .section-label {
    position: absolute;
    background: var(--paper);
    color: var(--brand-red);
    font-weight: 800;
    font-size: 8px;
    text-transform: uppercase;
    padding: 2px 8px;
    letter-spacing: .2px;
  }
  .section-label--large { font-size: 12px; padding: 3px 10px; }
  .label-choir { left: 18px; top: 428px; }
  .label-dates { left: 232px; top: 406px; background: none; color: var(--paper); padding: 0; }
  .label-hall { left: 412px; top: 8px; background: var(--ink); color: var(--brand-red); }
  .label-japan { left: 660px; top: 122px; }
  .label-europe { left: 430px; top: 292px; }
  .label-us { left: 680px; top: 346px; }

  .choir-copy { left: 18px; top: 456px; width: 202px; }
  .hall-copy { left: 412px; top: 28px; width: 180px; }
  .japan-copy { left: 612px; top: 142px; width: 182px; }
  .europe-copy { left: 430px; top: 312px; width: 180px; }
  .us-copy { left: 640px; top: 366px; width: 152px; }
</style>
</head>
<body>

<section class="spread spread--outer" aria-label="Brochure outer spread">
  <svg class="spread-art" viewBox="0 0 800 566">
    <defs>
      <linearGradient id="sunsetApron" x1="0" y1="0" x2="0" y2="1">
        <stop offset="0" stop-color="#f2c24a"/>
        <stop offset=".45" stop-color="#d98a3a"/>
        <stop offset="1" stop-color="#3d4e66"/>
      </linearGradient>
    </defs>
    <rect role="img" aria-label="Photo: airliner at the gate at sunset with travellers walking to board" x="40" y="90" width="720" height="340" fill="url(#sunsetApron)"/>
    <polygon points="100,30 800,0 800,95 330,95 300,135 100,75" fill="var(--brand-red)"/>
    <polygon points="0,400 420,372 560,445 560,566 0,566" fill="var(--ink)"/>
  </svg>
  <div class="fold"></div>

  <div class="brand-name cover-brand"><span>Meridian</span><span>Group Travel</span></div>

  <div class="brand-name back-brand"><span>Meridian</span><span>Group Travel</span></div>
  <ul class="contact-list">
    <li><span class="contact-icon"></span>(02) 9000 1234</li>
    <li><span class="contact-icon"></span>hello@meridiantours.example</li>
    <li><span class="contact-icon"></span>www.meridiantours.example</li>
  </ul>
</section>

<section class="spread spread--inner" aria-label="Brochure inner spread">
  <svg class="spread-art" viewBox="0 0 800 566">
    <rect x="0" y="0" width="800" height="566" fill="var(--ink)"/>
    <polygon points="172,0 400,0 400,380 60,425 60,200 172,125" fill="var(--paper)"/>
    <rect role="img" aria-label="Photo: gothic cathedral towers above a city square" x="228" y="424" width="172" height="142" fill="#8a9bb0"/>
    <polygon points="400,0 600,0 600,118 400,140" fill="var(--paper)"/>
    <rect role="img" aria-label="Photo: historic concert hall facade lit at night" x="600" y="0" width="200" height="116" fill="#5a3a1e"/>
    <rect role="img" aria-label="Photo: path through rows of red shrine gates" x="418" y="140" width="178" height="140" fill="#b23a22"/>
    <rect role="img" aria-label="Photo: ornate opera house interior with orchestra on stage" x="612" y="214" width="188" height="124" fill="#8a6a2e"/>
    <rect role="img" aria-label="Photo: marching band in red and white uniforms on a city street" x="430" y="420" width="200" height="146" fill="#6d4a44"/>
    <polygon points="640,566 800,470 800,566" fill="var(--brand-red)"/>
    <polygon points="400,566 430,520 430,566" fill="var(--brand-red-dark)"/>
  </svg>
  <div class="fold"></div>

  <div class="brand-name inner-brand"><span>Meridian</span><span>Group Travel</span></div>
  <p class="copy copy--light intro-lead">Meridian Group Travel was established in 2001 to provide once in a lifetime experiences.</p>

  <p class="copy copy--dark intro-focus">Our focus is providing unique opportunities to School &amp; Sports groups that expand the horizons of students, foster personal growth, develop independence and provide memories that last a lifetime.</p>
  <p class="copy copy--dark intro-body">Our understanding of the unique requirements of group travel and our personalised approach makes us the ideal choice in planning, sourcing and managing the perfect tour for your school or club. Our ever-growing global network allows us to offer exclusive experiences that are inaccessible to others. Our dedicated Tour Coordinators thoroughly consult with staff to tailor an itinerary and tour management plan that meets each unique set of requirements. We can assist in providing:</p>
  <ul class="service-list">
    <li>Customised Itineraries</li>
    <li>Negotiated Group Discounts on airfares, accommodation, transport and activities</li>
    <li>Festival/event entry</li>
    <li>Workshops with clinicians</li>
    <li>School exchanges</li>
    <li>Public performances</li>
    <li>Instrument rental</li>
    <li>Venue hire</li>
    <li>Trusted, Quality Suppliers</li>
    <li>Sightseeing</li>
    <li>Expert Guides and Tour Escorts</li>
  </ul>

  <p class="section-label label-dates">(5th to the 15th of July 2020)</p>
  <h2 class="section-label section-label--large label-choir">Global Choral Festival</h2>
  <p class="copy copy--light choir-copy">Join the biggest Choral Music event in the world with Choirs from over 80 different countries and regions, taking part in adjudicated performances, individual coaching and singing workshops. Held in Belgium in the cities Antwerp and Ghent, this is a fantastic opportunity to perform on the world stage as well as take in the rich history of the Flanders region. With the option to extend your trip to include France, Germany, Italy, Austria or other nearby European Countries.</p>

  <h2 class="section-label label-hall">Grand Concert Hall</h2>
  <p class="copy copy--dark hall-copy">The once in a life time opportunity to perform on one of the world's most famous music venues. Choirs will also have the opportunity to participate in performances, clinics, workshops and exchanges. Based in New York City, there will also be the chance to include stops in Washington DC, Los Angeles, or San Francisco on to your trip.</p>

  <h2 class="section-label label-japan">Japan Music Tours</h2>
  <p class="copy copy--light japan-copy">Travel to the land of the Rising Sun and take part in school exchanges, public performances and the chance to perform at famous Tokyo theme parks. Students will have the opportunity to take a Japanese Cooking Class, partake in a traditional Japanese Tea Ceremony, see a Kabuki show, and ride the bullet train.</p>

  <h2 class="section-label label-europe">European Instrumental Tours</h2>
  <p class="copy copy--light europe-copy">Play in Austria, France, Germany, the United Kingdom, or wherever your heart desires, you band, orchestra or ensemble will have the opportunity to perform at concert halls across Europe. As well as opportunities to participate in festivals, public performances and workshops with music professionals.</p>

  <h2 class="section-label label-us">US Music Road Trip</h2>
  <p class="copy copy--light us-copy">Trace a path across the US journeying from Jazz to Blues to Soul onto Rock n'Roll before finishing in Country Music capital of the world – Nashville. You will visit New Orleans, Memphis and Nashville where you will have the opportunity to perform at unique venues, undertake school exchanges and participate in workshops with musicians and professionals.</p>
</section>

</body>
</html>
```